Stationery Design Project

Letterhead with logo and address
Envelopes with Logo and address

The target market is start-ups and
small to medium businesses primarly located in China, with less than 20
employees. Please have designers use Yellow and Blue colors and our logo
attached. Looking fr the same format as the business card attached.

Reason: Designer has been delayed working on web design

Target Market(s)

Start-ups and small to medium size businesses

Industry/Entity Type

Business

Font styles to use
Sans Serif

Requirements
Must have
• None
Nice to have
• None
Should not have
• N/A

```html
<!DOCTYPE html>
<html lang="en">
<head>
<meta charset="UTF-8">
<title>NORTHBAY Stationery Set</title>
<link rel="stylesheet" href="https://fonts.googleapis.com/css2?family=Montserrat:wght@400;600&family=Noto+Sans+SC:wght@400&display=swap">
<style>
  :root {
    --navy: #1d4269;
    --navy-deep: #173858;
    --gold: #e6b421;
    --paper: #fbfbfb;
    --backdrop: #ececec;
    --ink: #2c3440;
    --ink-soft: #6b7480;
    --on-navy: #d8e1ec;
  }
  * { box-sizing: border-box; margin: 0; padding: 0; }
  html, body { width: 1200px; height: 858px; overflow: hidden; }
  body {
    background: var(--backdrop);
    font-family: "Montserrat", sans-serif;
    color: var(--ink);
    position: relative;
  }
  .sheet {
    position: absolute;
    background: var(--paper);
    box-shadow: 0 2px 6px rgba(0,0,0,0.12);
    overflow: hidden;
  }

  /* brand lockup: plain circle + name */
  .brand { display: flex; align-items: center; flex-direction: column; gap: 4px; }
  .brand-dot { display: block; border-radius: 50%; background: var(--gold); }
  .brand-name { font-weight: 400; color: var(--on-navy); letter-spacing: 0.18em; white-space: nowrap; }

  /* letterhead */
  .letterhead { left: 28px; top: 173px; width: 362px; height: 512px; }
  .side-band {
    position: absolute; left: 0; top: 0; bottom: 0;
    background: var(--navy);
    display: flex; flex-direction: column; justify-content: space-between; align-items: center;
  }
  .letterhead .side-band { width: 60px; padding: 14px 0 18px; }
  .letterhead .brand-dot { width: 22px; height: 22px; }
  .letterhead .brand-name { font-size: 5px; }
  .band-address {
    align-self: stretch;
    padding: 0 5px;
    font-size: 4.5px; line-height: 1.55; color: var(--on-navy);
    text-align: left;
    overflow-wrap: anywhere;
  }

  /* presentation folder */
  .folder {
    left: 420px; top: 173px; width: 362px; height: 512px;
    background: var(--navy);
    display: flex; flex-direction: column; align-items: center;
  }
  .folder .brand { margin-top: 150px; gap: 12px; }
  .folder .brand-dot { width: 62px; height: 62px; }
  .folder .brand-name { font-size: 17px; letter-spacing: 0.3em; color: #8ea4bf; }
  .folder-web {
    position: absolute; bottom: 70px; left: 50%; transform: translateX(-50%);
    font-size: 8px; color: var(--on-navy); letter-spacing: 0.04em; white-space: nowrap;
  }

  /* business card */
  .business-card { left: 812px; top: 173px; width: 200px; height: 114px; display: flex; }
  .card-strip {
    width: 52px; background: var(--navy);
    display: flex; flex-direction: column; align-items: center; justify-content: space-between;
    padding: 12px 3px 8px;
  }
  .card-strip .brand-dot { width: 16px; height: 16px; }
  .card-strip .brand-name { font-size: 4.5px; }
  .card-web { font-size: 3.8px; line-height: 1.4; color: var(--on-navy); text-align: center; }
  .card-body { flex: 1; padding: 16px 10px 8px 12px; text-align: right; }
  .card-name { font-size: 11px; font-weight: 600; color: var(--navy); }
  .card-title { font-size: 6px; color: var(--ink-soft); margin-bottom: 8px; }
  .card-company { font-family: "Noto Sans SC", sans-serif; font-size: 5px; color: var(--ink); margin-bottom: 3px; }
  .card-detail { font-size: 4.4px; line-height: 1.6; color: var(--ink-soft); }

  /* compliment slip */
  .slip { left: 812px; top: 311px; width: 360px; height: 170px; }
  .slip .side-band { width: 62px; padding: 14px 0 16px; }
  .slip .brand-dot { width: 24px; height: 24px; }
  .slip .brand-name { font-size: 5.5px; }
  .slip .band-address { font-size: 4.6px; }

  /* envelope */
  .envelope { left: 812px; top: 505px; width: 360px; height: 180px; }
  .envelope-flap {
    position: absolute; left: 0; right: 0; top: 0; height: 46px;
    background: var(--navy);
    display: flex; align-items: center; justify-content: center;
  }
  .envelope .brand { flex-direction: row; gap: 6px; }
  .envelope .brand-dot { width: 14px; height: 14px; }
  .envelope .brand-name { font-size: 7px; }
</style>
</head>
<body>

  <section class="sheet letterhead" aria-label="Letterhead">
    <div class="side-band">
      <div class="brand">
        <span class="brand-dot"></span>
        <span class="brand-name">NORTHBAY</span>
      </div>
      <p class="band-address">
        Room 1208,<br>
        Lianhe Tower<br>
        88 Century Avenue<br>
        Shanghai, China<br>
        +86 21 5555 0188<br>
        hello@<br>
        northbaypartners.com
      </p>
    </div>
  </section>

  <section class="sheet folder" aria-label="Presentation folder">
    <div class="brand">
      <span class="brand-dot"></span>
      <span class="brand-name">NORTHBAY</span>
    </div>
    <p class="folder-web">www.northbaypartners.com</p>
  </section>

  <section class="sheet business-card" aria-label="Business card">
    <div class="card-strip">
      <div class="brand">
        <span class="brand-dot"></span>
        <span class="brand-name">NORTHBAY</span>
      </div>
      <span class="card-web">www.northbay<br>partners.com</span>
    </div>
    <div class="card-body">
      <p class="card-name">Daniel Reyes</p>
      <p class="card-title">President &amp; CEO</p>
      <p class="card-company">北湾合伙人咨询（上海）有限公司</p>
      <p class="card-detail">
        Room 1208, Lianhe Tower, 88 Century Avenue<br>
        Shanghai 200120<br>
        +86 21 5555 0188<br>
        daniel@northbaypartners.com
      </p>
    </div>
  </section>

  <section class="sheet slip" aria-label="Compliment slip">
    <div class="side-band">
      <div class="brand">
        <span class="brand-dot"></span>
        <span class="brand-name">NORTHBAY</span>
      </div>
      <p class="band-address">
        Room 1208,<br>
        Lianhe Tower<br>
        88 Century Avenue<br>
        Shanghai, China<br>
        +86 21 5555 0188
      </p>
    </div>
  </section>

  <section class="sheet envelope" aria-label="Envelope">
    <div class="envelope-flap">
      <div class="brand">
        <span class="brand-dot"></span>
        <span class="brand-name">NORTHBAY</span>
      </div>
    </div>
  </section>

</body>
</html>
```